London based Blowdry bar needs drinks menu

Vorela Blowdry Bar is a successful trendy 'Blowdry bar' based in London. We offer our clients a number of services that are quick, affordable and ideal for a perfect night out!
Within the salon we offer soft & alcoholic drinks - I need to advertise this but space is limited. Therefore I would like to have a simple but pretty bar menu that will be designed like a banner and run under the mirrors at each position.
Please look at our website to have a look inside salon and pick up design ideas, colours used and feel of salon.
Website = www.example-glossquarter.co.uk
Font used for Vorela logo = Houschka rounded
Font used on website = District Pro
Measurement for each menu 90cm length x 7.5cm height (horizontal menu)
Target Market(s)
20-50 year olds - clients in salon to have a fast fun experience. needs to be clear, easy to read and to the point
Font styles to use
Other font styles liked:
- District Pro
Requirements
Must have
- Title of drink, price of drink - easy to read font
Nice to have
- Nice to have a picture of drink in beginning of menu (nice visual add) to draw attention to clients eyes and so they understand it is a drinks menu. Clear points at the beginning of each drink.

```html
<!DOCTYPE html>
<html lang="en">
<head>
<meta charset="utf-8">
<title>Vorela Blowdry Bar – Drinks Menu Banner</title>
<link rel="stylesheet" href="https://fonts.googleapis.com/css2?family=Didact+Gothic&display=swap">
<style>
  :root {
    --page-bg: #e6e7e8;
    --banner-bg: #ffffff;
    --ink: #1d1d24;
    --white: #ffffff;
    --orange-light: #f8b37a;
    --orange: #f39455;
    --pink-light: #f47fa6;
    --pink: #e9407a;
    --magenta: #ec4c9c;
    --magenta-deep: #e8337f;
    --rose-soft: #d977b3;
  }
  * { box-sizing: border-box; margin: 0; padding: 0; }
  html, body {
    width: 1200px; height: 507px; overflow: hidden;
    background: var(--page-bg);
    font-family: "Didact Gothic", "Helvetica Neue", Arial, sans-serif;
  }
  .menu-banner {
    position: absolute; left: 0; top: 116px;
    width: 1054px; height: 261px;
    background: var(--banner-bg);
    overflow: hidden;
  }
  .drink { position: absolute; top: 0; height: 100%; }
  .drink__art { position: absolute; }
  .drink__text { position: absolute; color: var(--ink); }
  .drink__name { font-size: 30px; line-height: 38px; letter-spacing: 0.2px; }
  .drink__price { display: flex; align-items: center; gap: 4px; font-size: 30px; line-height: 34px; }
  .drink__notes { font-size: 10.5px; line-height: 12px; }

  .drink--cocktails .drink__art { left: 8px; top: 62px; width: 146px; height: 140px; }
  .drink--cocktails .drink__text { left: 174px; top: 86px; }
  .drink--prosecco .drink__art { left: 340px; top: 66px; width: 130px; height: 134px; }
  .drink--prosecco .drink__text { left: 483px; top: 86px; }

  .offers {
    position: absolute; left: 672px; top: 0; width: 382px; height: 100%;
  }
  .offers__wash { position: absolute; inset: 0; }
  .offers__text {
    position: absolute; left: 112px; top: 76px;
    color: var(--white); font-size: 35px; line-height: 46px;
  }
</style>
</head>
<body>
  <section class="menu-banner" aria-label="Vorela Blowdry Bar drinks menu">

    <article class="drink drink--cocktails">
      <svg class="drink__art" viewBox="0 0 146 140" role="img" aria-label="Orange watercolour splash behind a cocktail glass icon">
        <defs>
          <radialGradient id="washOrange" cx="50%" cy="50%" r="55%">
            <stop offset="0" stop-color="var(--orange)"/>
            <stop offset="1" stop-color="var(--orange-light)" stop-opacity="0.75"/>
          </radialGradient>
        </defs>
        <path d="M20 20 C40 0 70 8 90 14 C118 10 140 30 138 60 C146 88 130 122 100 126 C80 140 50 136 30 124 C8 112 0 86 8 62 C2 44 8 30 20 20Z" fill="url(#washOrange)"/>
        <g fill="none" stroke="var(--white)" stroke-width="4" stroke-linecap="round" stroke-linejoin="round">
          <path d="M60 40 L96 40 L90 92 Q78 104 66 92 Z"/>
          <path d="M78 98 L78 120 M64 122 L92 122"/>
          <circle cx="100" cy="34" r="10"/>
          <path d="M76 40 L96 10"/>
          <path d="M24 40 L46 28"/>
        </g>
      </svg>
      <div class="drink__text">
        <h2 class="drink__name">Prosecco<br>Cocktails</h2>
        <p class="drink__price">£7 <span class="drink__notes">Elderflower, Peach,<br>Spritz &amp; Hibiscus</span></p>
      </div>
    </article>

    <article class="drink drink--prosecco">
      <svg class="drink__art" viewBox="0 0 130 134" role="img" aria-label="Pink watercolour splash behind a cocktail glass icon">
        <defs>
          <radialGradient id="washPink" cx="50%" cy="50%" r="55%">
            <stop offset="0" stop-color="var(--pink)"/>
            <stop offset="1" stop-color="var(--pink-light)" stop-opacity="0.8"/>
          </radialGradient>
        </defs>
        <path d="M16 18 C36 2 66 6 92 10 C120 16 128 44 122 68 C128 96 110 126 82 128 C58 134 30 124 18 104 C4 84 2 56 8 38 Z" fill="url(#washPink)"/>
        <g fill="none" stroke="var(--white)" stroke-width="4" stroke-linecap="round" stroke-linejoin="round">
          <path d="M24 40 L104 40 Q96 74 64 78 Q32 74 24 40 Z"/>
          <path d="M64 78 L64 116 M48 118 L80 118"/>
          <circle cx="34" cy="32" r="12"/>
          <path d="M80 40 L98 14"/>
        </g>
      </svg>
      <div class="drink__text">
        <h2 class="drink__name">Prosecco<br>/Rose Prosecco</h2>
        <p class="drink__price">£5</p>
      </div>
    </article>

    <aside class="offers">
      <svg class="offers__wash" viewBox="0 0 382 261" preserveAspectRatio="none" role="img" aria-label="Pink and magenta watercolour wash">
        <defs>
          <linearGradient id="washMagenta" x1="0" y1="0" x2="1" y2="1">
            <stop offset="0" stop-color="var(--magenta)"/>
            <stop offset="0.5" stop-color="var(--rose-soft)"/>
            <stop offset="1" stop-color="var(--magenta-deep)"/>
          </linearGradient>
        </defs>
        <path d="M0 0 L382 0 L382 261 L60 261 C70 240 50 220 64 196 C40 170 70 150 60 120 C30 100 40 70 20 50 C10 30 4 14 0 0Z" fill="url(#washMagenta)"/>
      </svg>
      <p class="offers__text">Check out bar<br>board for drink<br>offers...</p>
    </aside>

  </section>
</body>
</html>
```